Solarinho 4

Executive Corporate Housing Presentation (B2B Mobility Asset)
We are creating a Corporate Serviced Residence Pitch Deck for international corporate clients (e.g. Velnoria, global mobility teams, relocation departments).
The document is not a traditional real estate brochure. It is a B2B operational housing presentation designed for procurement, HR and corporate mobility decision-makers.
OBJECTIVE
The goal is to communicate:
Operational clarity
Corporate compliance readiness
Location feasibility
Building structure and usability
Executive-level accommodation standard
Reduced relocation and HR friction
DESIGN STYLE
The visual identity should be:
Clean corporate (Harbrook / Corvane / Velnoria style)
Minimalist, high whitespace
Structured and modular (not emotional storytelling)
Data + diagram driven
Subtle luxury (not hospitality marketing)
🚫AVOID
Real estate marketing style
Nestlyo / hospitality visuals
Overly emotional language or lifestyle imagery
Cluttered property listings
Dense technical architectural drawings
KEY VISUAL ELEMENT
Strong emphasis on:
Simplified building diagrams (hotel-style mapping)
Flow-based visuals (how users move through the building)
Corporate icons (access, parking, units, workspace)
Modular information blocks
DESIGN INTENT
The document should feel like:
“A corporate mobility solution presentation”
not
“a luxury property brochure”
Document will be around 12 pages long, I will provide all text and pictures. Enclosed an idea of the desired style. It has to be possible to make changes in the document (PDF - change renders to pictures & change the company's name if needed)
International corporate clients

```html
<!DOCTYPE html>
<html lang="en">
<head>
<meta charset="utf-8">
<title>Solarinho 4 — Corporate Residence Deck</title>
<link rel="stylesheet" href="https://fonts.googleapis.com/css2?family=Libre+Caslon+Text:wght@400&family=Montserrat:wght@400;500&display=swap">
<style>
:root{
  --page:#ebebec;
  --paper:#ffffff;
  --sand:#e3d8c6;
  --ink:#1f1d1b;
  --ink-soft:#3b3834;
  --muted:#9a958d;
  --rule:#cfc6b8;
  --serif:"Libre Caslon Text", Georgia, serif;
  --sans:"Montserrat", Arial, sans-serif;
}
*{box-sizing:border-box;margin:0;padding:0}
h1,h2,p{font-weight:400}
html,body{width:1200px;height:2270px;overflow:hidden;background:var(--page)}
.canvas{position:relative;width:1200px;height:2270px;font-family:var(--serif);color:var(--ink)}
.slide{position:absolute;width:320px;height:178px;background:var(--paper);overflow:hidden;box-shadow:9px 12px 18px rgba(0,0,0,.28)}
.slide > *{position:absolute}
.col-1{left:84px}.col-2{left:441px}.col-3{left:797px}
.row-1{top:704px}.row-2{top:919px}.row-3{top:1135px}.row-4{top:1351px}.row-5{top:1567px}.row-6{top:1783px}.row-7{top:2000px}

/* cover */
.cover{left:84px;top:81px;width:1032px;height:580px;box-shadow:12px 16px 26px rgba(0,0,0,.3)}
.cover-rail{left:0;top:0;width:81px;height:580px;background:var(--paper)}
.cover-panel{left:81px;top:0;width:951px;height:580px;background:var(--sand)}
.menu-icon{left:27px;top:26px;width:28px}
.menu-icon span{display:block;height:2px;background:var(--sand);margin-bottom:7px}
.rail-name{left:4px;top:360px;width:72px;transform:rotate(-90deg);text-align:center;font-size:13px;color:var(--sand);white-space:nowrap}
.rail-arrow{left:35px;top:435px}
.cover-kicker{left:81px;width:951px;top:94px;text-align:center;font-size:21px;letter-spacing:.5px}
.cover-title{left:81px;width:951px;top:232px;text-align:center;font-size:40px;line-height:52px;letter-spacing:.2px}
.cover-sub{left:81px;width:951px;top:420px;text-align:center;font-family:var(--sans);font-size:16.5px;line-height:24px;letter-spacing:.3px}

/* shared */
.sand{background:var(--sand)}
.heading{font-size:11px;line-height:12px;letter-spacing:.2px;text-transform:uppercase;color:var(--ink)}
.heading-lg{font-size:14px;line-height:15px;text-transform:uppercase}
.label{font-size:4.2px;letter-spacing:.3px;text-transform:uppercase;color:var(--ink-soft);white-space:nowrap}
.copy{font-size:3px;line-height:4.3px;color:var(--muted)}
.ring{width:16px;height:16px;border:.7px solid var(--muted);border-radius:50%;display:flex;align-items:center;justify-content:center;font-family:var(--sans);font-size:7px;color:var(--muted)}
.ring.small{width:12px;height:12px;font-size:5.5px}
.icon-ring{width:13px;height:13px;border-radius:50%;background:#efebe5;display:flex;align-items:center;justify-content:center}
.step{width:18px;height:18px;border-radius:50%;background:var(--sand);display:flex;align-items:center;justify-content:center;font-family:var(--sans);font-size:6px;color:var(--ink)}
.rule-v{width:.6px;background:var(--rule)}
.faint{color:#e9dfcf}
.flow-box{height:18px;background:#fff;display:flex;align-items:center;justify-content:center;font-size:4px;letter-spacing:.3px;text-transform:uppercase;color:var(--ink-soft)}
.floor{height:17px;border:.6px solid var(--rule);display:flex;align-items:center;justify-content:space-between;padding:0 5px;font-size:3.6px;letter-spacing:.3px;text-transform:uppercase;color:var(--ink-soft)}
.floor.accent{background:var(--sand);border-color:var(--sand)}

/* image areas */
.photo{display:block}
.ph-warm{background:linear-gradient(160deg,#d9c6ad,#8e7560)}
.ph-dark{background:linear-gradient(135deg,#2a2622,#6b5a47 55%,#1b1815)}
.ph-garden{background:linear-gradient(180deg,#9fb0a8 0%,#5f6b4f 55%,#3b3a2c 100%)}
.ph-sky{background:linear-gradient(180deg,#c9d6e0 0%,#e8e4dc 60%,#b9ad9b 100%)}
.ph-pool{background:linear-gradient(180deg,#7f8a6c 0%,#5b4a3d 55%,#4f9fb4 100%)}
.ph-interior{background:linear-gradient(150deg,#a89884,#4e4238 60%,#8b7d6c)}
.ph-blue{background:linear-gradient(180deg,#6d8fb8,#2f4a6a)}
.ph-person{background:linear-gradient(180deg,#d7d2cc,#8c7e73 60%,#2e2f45)}
</style>
</head>
<body>
<div class="canvas">

<!-- Cover -->
<section class="slide cover">
  <div class="cover-rail"></div>
  <div class="cover-panel"></div>
  <div class="menu-icon"><span></span><span></span><span></span></div>
  <div class="rail-name">Ellis Group</div>
  <svg class="rail-arrow" width="12" height="100" viewBox="0 0 12 100"><line x1="6" y1="0" x2="6" y2="96" stroke="#cfc6b8" stroke-width="1"/><path d="M3 92 L6 98 L9 92" fill="none" stroke="#cfc6b8" stroke-width="1"/></svg>
  <p class="cover-kicker">SOLARINHO 4</p>
  <h1 class="cover-title">WHERE HISTORY MEETS<br>FIVE UNIQUE DESIGNS</h1>
  <p class="cover-sub">MOVE-IN READY COMFORT, EFFORTLESS LIVING,<br>CURATED FOR PROFESSIONALS.</p>
</section>

<!-- Operator -->
<section class="slide col-1 row-1">
  <div class="photo ph-person" role="img" aria-label="Portrait of the operator lead" style="left:37px;top:35px;width:88px;height:109px"></div>
  <p class="label" style="left:38px;top:150px;font-size:3.6px">Founder</p>
  <div class="sand" style="left:166px;top:0;width:154px;height:178px"></div>
  <p style="left:190px;top:36px;font-size:8.5px">Mara Ellison</p>
  <p style="left:190px;top:49px;font-size:4.2px">Corporate residence operator</p>
  <p class="label" style="left:208px;top:83px">Operating model</p>
  <p class="copy" style="left:208px;top:92px;width:90px">Furnished units for relocating staff, ready on arrival, with clear monthly terms and one contact for every request.</p>
  <div style="left:208px;top:130px;width:28px;height:6px;background:#fff;font-size:2.6px;text-align:center;line-height:6px;color:var(--muted)">VIEW DETAILS</div>
</section>

<!-- Portfolio -->
<section class="slide col-2 row-1">
  <p class="label" style="left:29px;top:28px;font-size:6.5px">Residence portfolio</p>
  <svg style="left:220px;top:28px" width="32" height="6" viewBox="0 0 32 6"><line x1="0" y1="3" x2="30" y2="3" stroke="#1f1d1b" stroke-width=".5"/><path d="M28 1 L31 3 L28 5" fill="none" stroke="#1f1d1b" stroke-width=".5"/></svg>
  <div class="photo ph-warm" role="img" aria-label="Residence facade" style="left:23px;top:57px;width:82px;height:84px"></div>
  <div class="photo ph-garden" role="img" aria-label="Residence with garden" style="left:119px;top:57px;width:82px;height:84px"></div>
  <div class="photo ph-sky" role="img" aria-label="Residence exterior" style="left:214px;top:57px;width:82px;height:84px"></div>
  <p class="label" style="left:23px;top:151px;width:82px;text-align:center;font-size:3px">Units</p><p class="label" style="left:23px;top:158px;width:82px;text-align:center;font-size:3.6px">24</p>
  <p class="label" style="left:119px;top:151px;width:82px;text-align:center;font-size:3px">Parking</p><p class="label" style="left:119px;top:158px;width:82px;text-align:center;font-size:3.6px">18 bays</p>
  <p class="label" style="left:214px;top:151px;width:82px;text-align:center;font-size:3px">Airport</p><p class="label" style="left:214px;top:158px;width:82px;text-align:center;font-size:3.6px">25 min</p>
</section>

<!-- Building overview -->
<section class="slide col-3 row-1">
  <div class="photo ph-dark" role="img" aria-label="Staircase detail" style="left:136px;top:0;width:78px;height:66px"></div>
  <p class="heading faint" style="left:205px;top:18px;font-size:16px;line-height:17px">THE<br>BUILDING</p>
  <div class="photo ph-blue" role="img" aria-label="Building exterior" style="left:16px;top:72px;width:52px;height:78px"></div>
  <div class="photo ph-dark" role="img" aria-label="Interior detail" style="left:266px;top:88px;width:42px;height:62px"></div>
  <p class="label" style="left:101px;top:119px;font-size:3.6px">Overview</p>
  <p class="copy" style="left:101px;top:127px;width:140px">Each residence is listed with unit count, floor plan, parking and access details so teams can compare options quickly.</p>
</section>

<!-- Operating model -->
<section class="slide col-1 row-2">
  <h2 class="heading-lg" style="left:41px;top:25px">Our vision</h2>
  <p class="label" style="left:182px;top:43px;font-size:3.6px">Reducing relocation friction</p>
  <p class="label" style="left:38px;top:75px;font-size:3.6px">Operational clarity</p>
  <p class="copy" style="left:38px;top:84px;width:122px">Housing built for mobility teams: simple contracts, fixed monthly rates, secure access and workspace in every unit. Arrivals are planned with HR so new staff settle in on day one.</p>
  <p class="copy" style="left:170px;top:84px;width:122px">One point of contact for procurement and relocation, with clear reporting, compliance files and flexible stay lengths for every assignment in the building.</p>
  <div class="photo ph-dark" role="img" aria-label="Stair and light detail" style="left:0;top:142px;width:320px;height:36px"></div>
</section>

<!-- Location -->
<section class="slide col-2 row-2">
  <div class="sand" style="left:0;top:0;width:20px;height:178px"></div>
  <h2 class="heading" style="left:49px;top:42px">Location<br>feasibility</h2>
  <p class="label" style="left:47px;top:98px;font-size:3.6px">Travel times</p>
  <p class="copy" style="left:47px;top:107px;width:112px">Business district 10 min, airport 25 min, metro 4 min on foot. Schools, shops and clinics within a short walk.</p>
  <div class="photo ph-warm" role="img" aria-label="Street view of the residence" style="left:175px;top:0;width:116px;height:93px"></div>
  <div class="photo ph-pool" role="img" aria-label="Surrounding area" style="left:175px;top:103px;width:116px;height:60px"></div>
</section>

<!-- Unit standard -->
<section class="slide col-3 row-2">
  <div class="photo ph-interior" role="img" aria-label="Furnished bedroom" style="left:0;top:0;width:137px;height:178px"></div>
  <div class="sand" style="left:137px;top:10px;width:173px;height:168px"></div>
  <h2 class="heading" style="left:168px;top:38px">Executive<br>unit standard</h2>
  <div class="ring" style="left:282px;top:36px">↓</div>
  <p class="label" style="left:168px;top:89px;font-size:3.6px">Included in every unit</p>
  <p class="copy" style="left:168px;top:98px;width:108px">Bed, desk, kitchen and fast internet. Cleaning, linen and repairs handled on a set weekly plan.</p>
</section>

<!-- Corporate services with icons -->
<section class="slide col-1 row-3">
  <div class="sand" style="left:170px;top:0;width:150px;height:10px"></div>
  <h2 class="heading" style="left:34px;top:28px">Corporate<br>services</h2>
  <p class="label" style="left:32px;top:68px;font-size:3.6px">Core facilities</p>
  <p class="copy" style="left:32px;top:77px;width:120px">Access, parking and workspace are managed by one team on site.</p>
  <div class="photo ph-sky" role="img" aria-label="Building entrance" style="left:29px;top:112px;width:128px;height:66px"></div>
  <div class="icon-ring" style="left:190px;top:46px"><svg width="8" height="8" viewBox="0 0 8 8"><circle cx="2.3" cy="4" r="1.6" fill="none" stroke="#9a958d" stroke-width=".6"/><path d="M3.9 4 H7.5 M6.5 4 V5.4 M5.4 4 V5" stroke="#9a958d" stroke-width=".6" fill="none"/></svg></div>
  <p class="label" style="left:210px;top:46px;font-size:3px">Access</p>
  <p class="copy" style="left:210px;top:52px;width:90px">Key cards and 24/7 secure entry.</p>
  <div class="icon-ring" style="left:190px;top:91px"><svg width="8" height="8" viewBox="0 0 8 8"><rect x=".8" y=".8" width="6.4" height="6.4" fill="none" stroke="#9a958d" stroke-width=".6"/><path d="M3 6 V2 H4.6 A1.1 1.1 0 0 1 4.6 4.2 H3" fill="none" stroke="#9a958d" stroke-width=".6"/></svg></div>
  <p class="label" style="left:210px;top:91px;font-size:3px">Parking</p>
  <p class="copy" style="left:210px;top:97px;width:90px">Gated bays, one per unit.</p>
  <div class="icon-ring" style="left:190px;top:135px"><svg width="8" height="8" viewBox="0 0 8 8"><path d="M.8 3.6 H7.2 M1.6 3.6 V7 M6.4 3.6 V7" stroke="#9a958d" stroke-width=".6" fill="none"/><rect x="3" y="1" width="2.4" height="1.8" fill="none" stroke="#9a958d" stroke-width=".6"/></svg></div>
  <p class="label" style="left:210px;top:135px;font-size:3px">Workspace</p>
  <p class="copy" style="left:210px;top:141px;width:90px">Desks and meeting room on level 1.</p>
</section>

<!-- Arrival flow -->
<section class="slide col-2 row-3">
  <div class="sand" style="left:0;top:0;width:20px;height:178px"></div>
  <h2 class="heading-lg" style="left:47px;top:62px">Arrival<br>flow</h2>
  <p class="label" style="left:47px;top:98px;font-size:3.6px">Four steps</p>
  <svg style="left:0;top:0" width="320" height="178" viewBox="0 0 320 178"><path d="M169 29 L289 67 L168 107 L289 146" fill="none" stroke="#cfc6b8" stroke-width=".6" stroke-dasharray="2 2"/></svg>
  <div class="step" style="left:160px;top:20px">1</div>
  <p class="label" style="left:184px;top:21px;font-size:3px">Parking</p>
  <p class="copy" style="left:184px;top:27px;width:90px">Enter by card at the gate.</p>
  <div class="step" style="left:280px;top:58px">2</div>
  <p class="label" style="left:180px;top:59px;width:94px;text-align:right;font-size:3px">Lobby</p>
  <p class="copy" style="left:180px;top:65px;width:94px;text-align:right">Collect keys and welcome pack.</p>
  <div class="step" style="left:159px;top:98px">3</div>
  <p class="label" style="left:184px;top:99px;font-size:3px">Lift</p>
  <p class="copy" style="left:184px;top:105px;width:90px">Direct access to all floors.</p>
  <div class="step" style="left:280px;top:137px">4</div>
  <p class="label" style="left:180px;top:138px;width:94px;text-align:right;font-size:3px">Unit</p>
  <p class="copy" style="left:180px;top:144px;width:94px;text-align:right">Ready to live and work.</p>
</section>

<!-- Shared amenities -->
<section class="slide col-3 row-3">
  <div class="photo ph-warm" role="img" aria-label="Shared terrace" style="left:27px;top:34px;width:110px;height:66px"></div>
  <div class="photo ph-interior" role="img" aria-label="Shared lounge" style="left:49px;top:90px;width:110px;height:66px"></div>
  <h2 class="heading" style="left:184px;top:46px;width:108px;text-align:right">Shared<br>amenities</h2>
  <p class="label" style="left:184px;top:100px;font-size:3.6px">Common areas</p>
  <p class="copy" style="left:184px;top:109px;width:112px">Terrace, lounge, laundry and a meeting room are open to all residents, with set hours and bookings through the front desk.</p>
</section>

<!-- Booking process -->
<section class="slide col-1 row-4">
  <div class="sand" style="left:0;top:0;width:293px;height:178px"></div>
  <div style="left:304px;top:12px;width:8px"><div style="height:.6px;background:var(--rule);margin-bottom:1.6px"></div><div style="height:.6px;background:var(--rule);margin-bottom:1.6px"></div><div style="height:.6px;background:var(--rule)"></div></div>
  <h2 class="heading" style="left:24px;top:28px">Booking process</h2>
  <svg style="left:0;top:0" width="293" height="178" viewBox="0 0 293 178"><path d="M67 83 H138 M134 81 L138 83 L134 85 M162 83 H234 M230 81 L234 83 L230 85" fill="none" stroke="#9a958d" stroke-width=".6"/></svg>
  <div class="ring" style="left:47px;top:75px">1</div>
  <p class="label" style="left:25px;top:104px;width:60px;text-align:center;font-size:3.6px">Request</p>
  <p class="copy" style="left:25px;top:113px;width:60px;text-align:center">Send dates and team size.</p>
  <div class="ring" style="left:142px;top:75px">2</div>
  <p class="label" style="left:120px;top:104px;width:60px;text-align:center;font-size:3.6px">Match unit</p>
  <p class="copy" style="left:120px;top:113px;width:60px;text-align:center">We offer units by size and floor.</p>
  <div class="ring" style="left:238px;top:75px">3</div>
  <p class="label" style="left:216px;top:104px;width:60px;text-align:center;font-size:3.6px">Agreement</p>
  <p class="copy" style="left:216px;top:113px;width:60px;text-align:center">One contract for all your staff.</p>
</section>

<!-- Lot -->
<section class="slide col-2 row-4">
  <h2 class="heading" style="left:24px;top:22px">1.5 acre lot</h2>
  <p class="label" style="left:205px;top:18px;width:90px;text-align:right;font-size:3px">Site</p>
  <p class="copy" style="left:205px;top:24px;width:90px;text-align:right">Private grounds with gated parking and direct street access.</p>
  <div class="photo ph-sky" role="img" aria-label="Residence on its grounds" style="left:0;top:53px;width:320px;height:125px"></div>
</section>

<!-- Unit types -->
<section class="slide col-3 row-4">
  <div class="photo ph-sky" role="img" aria-label="Studio unit" style="left:0;top:0;width:64px;height:138px"></div>
  <div class="photo ph-garden" role="img" aria-label="One-bed unit" style="left:64px;top:0;width:64px;height:138px"></div>
  <div class="photo ph-warm" role="img" aria-label="Unit with office" style="left:128px;top:0;width:64px;height:138px"></div>
  <div class="photo ph-sky" role="img" aria-label="Executive unit" style="left:192px;top:0;width:64px;height:138px"></div>
  <div class="photo ph-blue" role="img" aria-label="Family unit" style="left:256px;top:0;width:64px;height:138px"></div>
  <div class="sand" style="left:0;top:138px;width:320px;height:40px"></div>
  <p class="label" style="left:10px;top:146px;font-size:3.6px;text-transform:none">Studio</p>
  <p class="copy" style="left:10px;top:153px;width:48px">Compact units for short stays.</p>
  <p class="label" style="left:74px;top:146px;font-size:3.6px;text-transform:none">One-bed</p>
  <p class="copy" style="left:74px;top:153px;width:48px">Bright units with open plans.</p>
  <p class="label" style="left:138px;top:146px;font-size:3.6px;text-transform:none">Work unit</p>
  <p class="copy" style="left:138px;top:153px;width:48px">Units with a separate office.</p>
  <p class="label" style="left:202px;top:146px;font-size:3.6px;text-transform:none">Executive</p>
  <p class="copy" style="left:202px;top:153px;width:48px">Large units for executives.</p>
  <p class="label" style="left:266px;top:146px;font-size:3.6px;text-transform:none">Family</p>
  <p class="copy" style="left:266px;top:153px;width:48px">Two beds for longer stays.</p>
</section>

<!-- Compliance pack -->
<section class="slide col-1 row-5">
  <div class="photo ph-pool" role="img" aria-label="Residence grounds" style="left:0;top:0;width:320px;height:178px"></div>
  <div style="left:52px;top:57px;width:227px;height:66px;background:#fff"></div>
  <div class="ring" style="left:67px;top:82px">↓</div>
  <p style="left:93px;top:84px;font-size:10px">Compliance - document pack</p>
</section>

<!-- Site gallery -->
<section class="slide col-2 row-5">
  <p class="label" style="left:24px;top:20px;font-size:3px">Site</p>
  <p class="copy" style="left:24px;top:26px;width:90px">Grounds, pool and parking on one private lot.</p>
  <h2 class="heading" style="left:200px;top:27px;width:94px;text-align:right">1.5 acre lot</h2>
  <div class="photo ph-garden" role="img" aria-label="Building among trees" style="left:22px;top:62px;width:66px;height:100px"></div>
  <div class="photo ph-sky" role="img" aria-label="Building facade" style="left:94px;top:62px;width:66px;height:100px"></div>
  <div class="photo ph-pool" role="img" aria-label="Pool area" style="left:190px;top:62px;width:112px;height:68px"></div>
  <p class="label" style="left:224px;top:152px;font-size:3px">Site plan</p>
  <div class="ring small" style="left:282px;top:147px">→</div>
</section>

<!-- HR friction -->
<section class="slide col-3 row-5">
  <div class="photo ph-sky" role="img" aria-label="Garden and sky" style="left:0;top:0;width:320px;height:178px"></div>
  <div style="left:0;top:22px;width:297px;height:156px;background:#fff"></div>
  <p class="label" style="left:40px;top:52px;font-size:3px">For HR teams</p>
  <p class="copy" style="left:40px;top:58px;width:90px">Fewer calls, faster moves.</p>
  <h2 class="heading" style="left:180px;top:60px;width:102px;text-align:right">Less HR<br>friction</h2>
  <p class="label" style="left:40px;top:109px;font-size:3.6px">One agreement</p>
  <p class="copy" style="left:40px;top:118px;width:215px">A single agreement covers all staff, with fixed rates, monthly invoices and clear rules for arrivals and departures. Our team handles keys, cleaning and repairs so HR teams do not have to.</p>
  <div class="ring" style="left:278px;top:144px">↓</div>
</section>

<!-- Building structure diagram -->
<section class="slide col-1 row-6">
  <div class="sand" style="left:0;top:0;width:320px;height:46px"></div>
  <h2 class="heading" style="left:32px;top:26px;font-size:10px">Building structure</h2>
  <p class="label" style="left:31px;top:70px;font-size:3.6px">Floor mapping</p>
  <p class="copy" style="left:31px;top:79px;width:100px">Five levels with one lift core. Parking below, lobby and workspace at street level, units above.</p>
  <div class="floor" style="left:160px;top:56px;width:130px"><span>Level 3</span><span>8 units</span></div>
  <div class="floor" style="left:160px;top:76px;width:130px"><span>Level 2</span><span>8 units</span></div>
  <div class="floor" style="left:160px;top:96px;width:130px"><span>Level 1</span><span>8 units · workspace</span></div>
  <div class="floor accent" style="left:160px;top:116px;width:130px"><span>Ground</span><span>Lobby · reception</span></div>
  <div class="floor" style="left:160px;top:136px;width:130px;border-style:dashed"><span>Level -1</span><span>Parking · 18 bays</span></div>
  <div style="left:150px;top:56px;width:4px;height:97px;background:var(--ink-soft)"></div>
  <p class="label" style="left:140px;top:157px;font-size:3px">Lift core</p>
</section>

<!-- Workspace -->
<section class="slide col-2 row-6">
  <div class="photo ph-pool" role="img" aria-label="Workspace area" style="left:25px;top:14px;width:116px;height:55px"></div>
  <h2 class="heading" style="left:181px;top:42px">Workspace</h2>
  <div class="rule-v" style="left:28px;top:111px;height:48px"></div>
  <p class="label" style="left:46px;top:111px;font-size:3.6px">Work from the building</p>
  <p class="copy" style="left:46px;top:120px;width:180px">Shared desks, a bookable meeting room and print corner on level 1, plus a desk and fast internet in every unit.</p>
  <div class="photo ph-pool" role="img" aria-label="Meeting room" style="left:270px;top:96px;width:50px;height:80px"></div>
</section>

<!-- User flow -->
<section class="slide col-3 row-6">
  <div class="sand" style="left:0;top:0;width:320px;height:178px"></div>
  <div style="left:34px;top:0;width:285px;height:66px;background:#fff"></div>
  <div class="ring small" style="left:55px;top:33px">↓</div>
  <h2 class="heading" style="left:79px;top:35px;font-size:10px">How users move</h2>
  <p class="label" style="left:46px;top:80px;font-size:3.6px">Daily flow</p>
  <div class="flow-box" style="left:46px;top:92px;width:50px">Parking</div>
  <div class="flow-box" style="left:112px;top:92px;width:50px">Lobby</div>
  <div class="flow-box" style="left:178px;top:92px;width:50px">Lift core</div>
  <div class="flow-box" style="left:244px;top:92px;width:50px">Unit</div>
  <svg style="left:0;top:0" width="320" height="178" viewBox="0 0 320 178"><path d="M98 101 H110 M107 99 L110 101 L107 103 M164 101 H176 M173 99 L176 101 L173 103 M230 101 H242 M239 99 L242 101 L239 103" fill="none" stroke="#3b3834" stroke-width=".6"/></svg>
  <p class="copy" style="left:46px;top:124px;width:248px">Residents reach their unit from the car park in under two minutes. Visitors check in at the lobby, and service staff use a separate rear entrance to the lift core.</p>
</section>

<!-- Support model -->
<section class="slide col-1 row-7">
  <div class="photo ph-warm" role="img" aria-label="Garden wall" style="left:0;top:0;width:320px;height:40px"></div>
  <h2 class="heading" style="left:30px;top:60px">Support<br>model</h2>
  <div class="ring" style="left:30px;top:128px">↓</div>
  <p class="label" style="left:100px;top:131px;width:107px;text-align:right;font-size:3.6px">Single contact</p>
  <p class="copy" style="left:100px;top:139px;width:107px;text-align:right">One manager for all requests, 7 days a week.</p>
  <div class="photo ph-pool" role="img" aria-label="Reception area" style="left:218px;top:73px;width:77px;height:75px"></div>
</section>

<!-- Unit gallery -->
<section class="slide col-2 row-7">
  <h2 class="heading" style="left:26px;top:22px">Unit<br>gallery</h2>
  <p class="label" style="left:166px;top:28px;font-size:3px">Renders</p>
  <p class="copy" style="left:166px;top:34px;width:90px">Images of each unit type, updated as fit-out is complete.</p>
  <div class="photo ph-pool" role="img" aria-label="Unit view" style="left:22px;top:70px;width:60px;height:52px"></div>
  <div class="photo ph-interior" role="img" aria-label="Living room" style="left:92px;top:90px;width:60px;height:45px"></div>
  <div class="photo ph-interior" role="img" aria-label="Dining area" style="left:163px;top:70px;width:60px;height:52px"></div>
  <div class="photo ph-pool" role="img" aria-label="Balcony view" style="left:236px;top:70px;width:60px;height:62px"></div>
  <p class="label" style="left:22px;top:143px;font-size:3px">Property</p>
  <div class="ring" style="left:274px;top:147px">↓</div>
</section>

<!-- Contract terms -->
<section class="slide col-3 row-7">
  <div class="photo ph-pool" role="img" aria-label="Building exterior" style="left:0;top:0;width:45px;height:178px"></div>
  <div class="photo ph-warm" role="img" aria-label="Garden wall" style="left:195px;top:0;width:75px;height:18px"></div>
  <h2 class="heading" style="left:81px;top:35px">Contract<br>terms</h2>
  <div class="rule-v" style="left:93px;top:118px;height:34px"></div>
  <p class="label" style="left:111px;top:102px;font-size:3.6px">Compliance ready</p>
  <p class="copy" style="left:111px;top:111px;width:190px">Stays from one month, a fixed monthly rate and one invoice per company. Insurance, safety checks and guest registration are kept on file for audit.</p>
</section>

</div>
</body>
</html>
```